Copper Lantern - website for leadership service

I would like help to use a Squarespace template for a simple website.
We already have a logo which will influence the colour choice and tone.
Clean lines for executive audience. it is an exclusive service. I have all the content ready to go.
Would like some images included.

I will upload the content soon.

Does NOT need SEO as it will be direct mailed. Also does NOT need to consider having any payment pages or enquiry form.
Thanks

Target Market(s)

Women executives - senior leaders. Stylish, serious and capable.

Coding

Coded - Design and coding required

Number of Pages Required

3 page

Colors
3176b5
fee18a

Requirements
Must have
• Sqaurespace template. And scrolling down page format.

To suit style of the blue and gold logo.
Nice to have
• Simple, Stylish and exclusive feel. Inspiring but not "New Age"
Should not have
• Too many colours.

No

```html
<!DOCTYPE html>
<html lang="en">
<head>
<meta charset="utf-8">
<title>Copper Lantern</title>
<link href="https://fonts.googleapis.com/css2?family=IBM+Plex+Sans:wght@400;500;600;700&display=swap" rel="stylesheet">
<style>
:root{
  --blue:#2962ab;
  --gold:#f2d57c;
  --gold-line:#c9a443;
  --ink:#111111;
  --body:#2b2b2b;
  --mist:#f4f1f1;
  --white:#ffffff;
  --btn-ink:#3a2d0c;
}
*{margin:0;padding:0;box-sizing:border-box}
html,body{width:1200px;height:2931px;overflow:hidden}
body{font-family:"IBM Plex Sans",Arial,sans-serif;color:var(--ink);background:var(--white);position:relative}
.section{position:absolute;left:0;width:1200px}
/* hero */
.hero{top:0;height:694px;background:linear-gradient(100deg,#3a2a2c 0%,#b8552e 30%,#d7743d 45%,#6b5c6a 62%,#2a2f45 80%,#1c2236 100%)}
.hero-photo{position:absolute;inset:0}
.hero::before{content:"";position:absolute;left:0;top:0;width:100%;height:140px;background:linear-gradient(#1b2236,rgba(27,34,54,0))}
.brand{position:absolute;left:136px;top:42px;z-index:2;color:var(--white);font-size:18px;font-weight:500}
.nav{position:absolute;right:131px;top:31px;display:flex;gap:37px;z-index:2}
.nav a{color:var(--white);text-decoration:none;font-weight:600;font-size:14px;letter-spacing:.3px}
.nav a.current{color:var(--gold);text-decoration:underline;text-underline-offset:3px}
.hero-title{position:absolute;top:272px;width:100%;text-align:center;color:var(--white);font-size:56px;font-weight:700;letter-spacing:.5px;text-shadow:0 2px 6px rgba(0,0,0,.35)}
.btn{display:inline-block;background:var(--gold);color:var(--btn-ink);font-weight:700;font-size:18px;letter-spacing:.4px;text-align:center;text-decoration:none}
.hero .btn{position:absolute;left:530px;top:364px;width:141px;height:43px;line-height:39px;border:2px solid var(--gold-line)}
/* headings */
.sec-title{position:absolute;left:131px;font-size:28px;font-weight:700;letter-spacing:.3px}
.arrows{position:absolute;left:1026px;display:flex;gap:8px}
.arrows svg{width:18px;height:24px}
/* resources */
.resources{top:694px;height:556px;background:var(--white)}
.res-card{position:absolute;top:127px;width:299px;text-align:center}
.res-img{width:299px;height:229px}
.res-card h3{font-size:16px;font-weight:700;line-height:17.5px;margin-top:26px;letter-spacing:.2px}
.res-card p{font-size:13px;line-height:16px;color:var(--body);margin:8px auto 0;width:230px}
/* about */
.about{top:1250px;height:560px;background:var(--blue);color:var(--white)}
.about-img{position:absolute;left:133px;top:57px;width:497px;height:449px;background:linear-gradient(160deg,#8a5a48 0%,#c9b9ad 40%,#6f6a73 60%,#2b2a33 100%)}
.about h2{position:absolute;left:708px;top:118px;font-size:28px;font-weight:700;letter-spacing:.3px}
.about p{position:absolute;left:708px;top:181px;width:310px;font-size:19.5px;line-height:25.6px;font-weight:400}
.about .btn{position:absolute;left:710px;top:379px;width:143px;height:46px;line-height:46px}
/* testimonials */
.testimonials{top:1810px;height:527px;background:var(--mist)}
.quote-card{position:absolute;top:130px;width:299px;height:333px;background:var(--white);text-align:center;box-shadow:0 0 3px rgba(0,0,0,.05)}
.quote-card p{font-size:13px;line-height:16px;color:var(--body);margin:53px auto 0;width:222px}
.quote-card .who{position:absolute;left:0;top:261px;width:100%;font-size:12px;font-weight:700;line-height:16px;text-transform:uppercase}
/* contact */
.contact{top:2337px;height:320px;background:var(--white)}
.contact h2{position:absolute;left:343px;top:130px;font-size:28px;font-weight:700;letter-spacing:.3px}
.contact-info{position:absolute;left:658px;font-size:20px;line-height:26px;color:var(--ink)}
.contact-info .label{font-weight:500}
/* footer */
.footer{top:2657px;height:274px;background:var(--blue);color:var(--white);text-align:center}
.foot-nav{position:absolute;top:69px;width:100%;display:flex;justify-content:center;gap:38px}
.foot-nav a{color:var(--white);text-decoration:none;font-weight:600;font-size:14px;letter-spacing:.3px}
.socials{position:absolute;top:128px;width:100%;display:flex;justify-content:center;gap:9px}
.social{width:34px;height:34px;border-radius:50%}
.social.s1{background:#3b4fa8}
.social.s2{background:#27a4e8}
.social.s3{background:#1f1f5a}
.copyright{position:absolute;top:198px;width:100%;font-size:12px}
</style>
</head>
<body>

<header class="section hero">
  <div class="hero-photo" role="img" aria-label="Woman presenting at a laptop to a large conference audience"></div>
  <div class="brand">Copper Lantern</div>
  <nav class="nav">
    <a class="current" href="#about">ABOUT</a>
    <a href="#testimonials">TESTIMONIALS</a>
    <a href="#resources">RESOURCES</a>
    <a href="#contact">CONTACT</a>
  </nav>
  <h1 class="hero-title">NEW ERA OF BUSINESS</h1>
  <a class="btn" href="#about">READ MORE</a>
</header>

<section class="section resources" id="resources">
  <h2 class="sec-title" style="top:64px">RESOURCES</h2>
  <div class="arrows" style="top:70px">
    <svg viewBox="0 0 18 24"><path d="M13 3 L5 12 L13 21" fill="none" stroke="#555" stroke-width="2.2"/></svg>
    <svg viewBox="0 0 18 24"><path d="M5 3 L13 12 L5 21" fill="none" stroke="#555" stroke-width="2.2"/></svg>
  </div>
  <article class="res-card" style="left:133px">
    <div class="res-img" role="img" aria-label="Audience applauding at a conference" style="background:linear-gradient(135deg,#5a3a30,#c58a6a 50%,#3a2a28)"></div>
    <h3>EXECUTIVE FORUM 2019</h3>
    <p>Executive Forum today announced the release of a new Statement on the Purpose of a Corporation signed by 181 CEOs</p>
  </article>
  <article class="res-card" style="left:450px">
    <div class="res-img" role="img" aria-label="Hands writing notes at a meeting table" style="background:linear-gradient(135deg,#2f2f36,#8a7e78 50%,#c9b9a4)"></div>
    <h3>THESE FOUR LEADERSHIP<br>MINDSETS ARE DRIVING<br>THE NEW ECONOMY</h3>
    <p>Are you able to change the culture of your organization?</p>
  </article>
  <article class="res-card" style="left:770px">
    <div class="res-img" role="img" aria-label="Large crowd seated in an auditorium" style="background:linear-gradient(180deg,#b79a80,#5a3f5a 45%,#231a28)"></div>
    <h3>MARCUS HALDEN</h3>
    <p>The “new capitalism” happens when companies act on behalf of both shareholders and stakeholders</p>
  </article>
</section>

<section class="section about" id="about">
  <div class="about-img" role="img" aria-label="Speaker on stage addressing a seated audience"></div>
  <h2>ABOUT HELENA</h2>
  <p>Helena is a highly experienced executive coach, business woman and thought leader in leadership for change. She is widely respected for her astute commercial and strategic acumen.</p>
  <a class="btn" href="#about">READ MORE</a>
</section>

<section class="section testimonials" id="testimonials">
  <h2 class="sec-title" style="top:58px">TESTIMONIALS</h2>
  <div class="arrows" style="top:64px">
    <svg viewBox="0 0 18 24"><path d="M13 3 L5 12 L13 21" fill="none" stroke="#555" stroke-width="2.2"/></svg>
    <svg viewBox="0 0 18 24"><path d="M5 3 L13 12 L5 21" fill="none" stroke="#555" stroke-width="2.2"/></svg>
  </div>
  <article class="quote-card" style="left:133px">
    <p>I have had the pleasure of spending the last year working with Helena. Her measured guidance has been a pillar for my success this year. She helped me to find my voice and gave me the confidence to speak up where needed. Helena has helped me to prioritise my time to become more of a leader and less of an administrator. I feel so much more confident in my role with a clear vision into the future.</p>
    <div class="who">Claire Donovan<br>CEO at Harbour Light Foundation</div>
  </article>
  <article class="quote-card" style="left:452px">
    <p>I had the pleasure of being able to enjoy the benefits of executive coaching with Helena. The insights and guidance Helena provided into my development has helped me immensely both personally and professionally and I can’t recommend her enough for any person wanting to move forward with their journey.</p>
    <div class="who">Rachel Amberly<br>General Manager</div>
  </article>
  <article class="quote-card" style="left:770px">
    <p>Helena has a style of coaching that is both supportive and challenging. Her style helps explore the possible in a planned and constructive manner - helping to push you forward and widen your perspective. Very valuable discussions.</p>
    <div class="who">Joanna Merritt<br>Chief Executive Officer at the Property<br>Guild of Aotearoa</div>
  </article>
</section>

<section class="section contact" id="contact">
  <h2>CONTACT</h2>
  <div class="contact-info" style="top:77px"><div class="label">Email</div><div>example@example.com</div></div>
  <div class="contact-info" style="top:172px"><div class="label">Address</div><div style="margin-top:6px">123 Demo Street<br>New York, NY 12345</div></div>
</section>

<footer class="section footer">
  <nav class="foot-nav">
    <a href="#about">ABOUT</a>
    <a href="#testimonials">TESTIMONIALS</a>
    <a href="#resources">RESOURCES</a>
    <a href="#contact">CONTACT</a>
  </nav>
  <div class="socials">
    <span class="social s1" role="img" aria-label="Social link one"></span>
    <span class="social s2" role="img" aria-label="Social link two"></span>
    <span class="social s3" role="img" aria-label="Social link three"></span>
  </div>
  <div class="copyright">Copyright © 2020 All Rights Reserved</div>
</footer>

</body>
</html>
```